Drug Company Needs a Counter Display

********I am after a point of sale counter top display design. **********
^^^^^^^^^^^^^^^^^^^^^^^^^^^^^^^^^^^^^^^^^^^^^^^^^^

The design should somewhat match the current format of my products, be eye caching and modern. PLEASE REFERR TO THE ATTACHMENTS FOR INSPIRATION

What I had in mind for this project was;
If you can notice the counter display as shown in the picture with the products inside.
The bottom half of the product boxes have been cut off because of the front lip of the display, I was perhaps thinking that the display could have the bottom half of the box printed on it so it would give the illusion of a complete box.. This could be the same on the sides also, as it tapers up giving the illusion of a complete box.

I imagine possibly having the centre divider either black on the centre and then because the display is slightly larger than the boxes the "illusion" box on the left and right can be centered and then outlined with black lines.

The header board should have a clear catch phrase like "Drug Testing Kits"- easy to use -99% accuracy - fast results the text can be set on a contrasting background, solid colors are ok with gradients, swirls etc any graphic you think looks good.

Detection Times
*Depending on quantity
Ecstasy - 1 - 3 Days
Meth Amphetamine - 1 - 3 Days
Marijuana - 1 - 30 Days

This project is very open to creativity and designers can head in their own direction with this, I am not overly creative and my idea was only a suggestion.. I am keen to take on any eye catching yet professional design.

Thanks in advance.

Target Market(s)

Adults ages 18 - 45 in western speaking countries.

Industry/Entity Type

Drug

Requirements
Must have
• Easy to read text
Should not have
• cluttered text

```html
<!DOCTYPE html>
<html lang="en">
<head>
<meta charset="utf-8">
<title>Drug Testing Kit – Counter Display Dieline</title>
<link rel="stylesheet" href="https://fonts.googleapis.com/css2?family=Archivo+Black&family=Oswald:wght@500;700&family=Roboto:wght@400;700&display=swap">
<style>
  :root{
    --paper:#ffffff;
    --cut:#e8372c;
    --fold:#39d44a;
    --ink:#111111;
    --red:#f04a1e;
    --header-red:#e3401c;
    --green:#48d41c;
    --lime:#c9f02a;
    --navy:#0a1a8c;
    --sky:#1fc6ee;
    --blue-ink:#1a2a9c;
    --board:#0b0b0b;
  }
  html,body{margin:0;padding:0;overflow:hidden;background:var(--paper);}
  .canvas{width:1200px;height:1000px;position:relative;overflow:hidden;background:var(--paper);}
  .dieline{display:block;width:1200px;height:1000px;}
  .cut{fill:none;stroke:var(--cut);stroke-width:1.2;}
  .fold{fill:none;stroke:var(--fold);stroke-width:1.2;}
  .title{font-family:"Archivo Black",sans-serif;font-size:38px;fill:#fff;stroke:var(--navy);stroke-width:4px;paint-order:stroke;stroke-linejoin:round;letter-spacing:1px;}
  .slogan{font-family:"Roboto",sans-serif;font-weight:700;font-size:18px;fill:#1e4a10;}
  .detect-head{font-family:"Roboto",sans-serif;font-weight:700;font-size:15px;fill:#0d2a06;letter-spacing:1px;}
  .detect-list{font-family:"Roboto",sans-serif;font-weight:700;font-size:13px;fill:#fff;}
  .footnote{font-family:"Roboto",sans-serif;font-size:9px;fill:var(--blue-ink);}
  .spine{font-family:"Oswald",sans-serif;font-weight:700;font-size:18px;fill:#fff;}
  .spine-dark{font-family:"Oswald",sans-serif;font-weight:500;font-size:9px;fill:var(--ink);}
  .brand{font-family:"Oswald",sans-serif;font-weight:700;font-size:10px;fill:var(--ink);}
  .box-word{font-family:"Oswald",sans-serif;font-weight:700;font-size:28px;fill:#fff;}
  .box-name{font-family:"Roboto",sans-serif;font-weight:700;font-size:10px;fill:var(--ink);}
  .box-small{font-family:"Roboto",sans-serif;font-size:5px;fill:var(--ink);}
</style>
</head>
<body>
<main class="canvas">
<svg class="dieline" viewBox="0 0 1200 1000" xmlns="http://www.w3.org/2000/svg">
  <defs>
    <linearGradient id="titleGradient" x1="0" x2="1">
      <stop offset="0" stop-color="var(--sky)"/>
      <stop offset="0.2" stop-color="var(--navy)"/>
      <stop offset="0.8" stop-color="var(--navy)"/>
      <stop offset="1" stop-color="var(--sky)"/>
    </linearGradient>
    <radialGradient id="sloganGradient" cx="0.5" cy="0.5" r="0.6">
      <stop offset="0" stop-color="#f2fb7a"/>
      <stop offset="1" stop-color="var(--lime)"/>
    </radialGradient>
    <clipPath id="clipThreeInOne"><rect x="350" y="845" width="210" height="115"/></clipPath>
  </defs>

  <!-- header board -->
  <g class="header-board">
    <path class="cut" d="M343 437 V48 Q343 40 351 40 H775 Q783 40 783 48 V437"/>
    <line class="cut" x1="563" y1="40" x2="563" y2="185"/>
    <line class="cut" x1="568" y1="40" x2="568" y2="185"/>
    <g class="header-art" transform="rotate(180 565.5 248)">
      <rect x="338" y="181" width="455" height="53" fill="url(#titleGradient)"/>
      <text class="title" x="565" y="222" text-anchor="middle">Drug Testing Kit</text>
      <rect x="338" y="234" width="455" height="25" fill="url(#sloganGradient)"/>
      <text class="slogan" x="565" y="253" text-anchor="middle">easy to use - 99% accuracy - fast results</text>
      <rect x="338" y="259" width="455" height="19" fill="var(--green)"/>
      <text class="detect-head" x="565" y="274" text-anchor="middle">Detection Times</text>
      <rect x="338" y="278" width="455" height="37" fill="var(--header-red)"/>
      <text class="detect-list" x="565" y="297" text-anchor="middle" textLength="436" lengthAdjust="spacingAndGlyphs">Ecstasy - 1 - 3 Days | Meth Amphetamine - 1 - 3 Days | Marijuana - 1 - 30 Days</text>
      <text class="footnote" x="565" y="310" text-anchor="middle">*Depending on quantity</text>
    </g>
  </g>

  <!-- front lip and base -->
  <g class="front-and-base">
    <rect class="fold" x="345" y="437" width="440" height="148"/>
    <rect class="fold" x="345" y="585" width="440" height="260"/>
    <path class="cut" d="M345 437 L196 492 V585"/>
    <path class="cut" d="M785 437 L935 492 V585"/>
    <rect class="cut" x="344" y="660" width="8" height="110" rx="4"/>
    <rect class="cut" x="778" y="660" width="8" height="110" rx="4"/>
    <path class="cut" d="M196 585 L80 680 L125 737 L121 745 L240 878 L290 845"/>
    <path class="cut" d="M935 585 L1051 680 L1006 737 L1010 745 L891 878 L840 845"/>
    <path class="cut" d="M290 845 V900 H345"/>
    <path class="cut" d="M840 845 V900 H785"/>
  </g>

  <!-- left side wall: stacked box ends -->
  <g class="side-left">
    <rect x="196" y="588" width="47" height="252" fill="var(--navy)"/>
    <rect x="243" y="588" width="45" height="252" fill="var(--green)"/>
    <rect x="288" y="588" width="57" height="252" fill="var(--red)"/>
    <g class="row-lines" stroke="#fff" stroke-width="2">
      <line x1="196" y1="610" x2="345" y2="610"/><line x1="196" y1="633" x2="345" y2="633"/>
      <line x1="196" y1="656" x2="345" y2="656"/><line x1="196" y1="679" x2="345" y2="679"/>
      <line x1="196" y1="702" x2="345" y2="702"/><line x1="196" y1="725" x2="345" y2="725"/>
      <line x1="196" y1="748" x2="345" y2="748"/><line x1="196" y1="771" x2="345" y2="771"/>
      <line x1="196" y1="794" x2="345" y2="794"/><line x1="196" y1="817" x2="345" y2="817"/>
    </g>
    <g class="spine">
      <text x="219" y="606" text-anchor="middle">IC</text><text x="265" y="606" text-anchor="middle">TE</text><text x="316" y="606" text-anchor="middle">M</text>
      <text x="219" y="629" text-anchor="middle">IC</text><text x="265" y="629" text-anchor="middle">TE</text><text x="316" y="629" text-anchor="middle">M</text>
      <text x="219" y="652" text-anchor="middle">IC</text><text x="265" y="652" text-anchor="middle">TE</text><text x="316" y="652" text-anchor="middle">M</text>
      <text x="219" y="675" text-anchor="middle">IC</text><text x="265" y="675" text-anchor="middle">TE</text><text x="316" y="675" text-anchor="middle">M</text>
      <text x="219" y="698" text-anchor="middle">IC</text><text x="265" y="698" text-anchor="middle">TE</text><text x="316" y="698" text-anchor="middle">M</text>
      <text x="219" y="721" text-anchor="middle">IC</text><text x="265" y="721" text-anchor="middle">TE</text><text x="316" y="721" text-anchor="middle">M</text>
      <text x="219" y="744" text-anchor="middle">IC</text><text x="265" y="744" text-anchor="middle">TE</text><text x="316" y="744" text-anchor="middle">M</text>
      <text x="219" y="767" text-anchor="middle">IC</text><text x="265" y="767" text-anchor="middle">TE</text><text x="316" y="767" text-anchor="middle">M</text>
      <text x="219" y="790" text-anchor="middle">IC</text><text x="265" y="790" text-anchor="middle">TE</text><text x="316" y="790" text-anchor="middle">M</text>
      <text x="219" y="813" text-anchor="middle">IC</text><text x="265" y="813" text-anchor="middle">TE</text><text x="316" y="813" text-anchor="middle">M</text>
      <text x="219" y="836" text-anchor="middle">IC</text><text x="265" y="836" text-anchor="middle">TE</text><text x="316" y="836" text-anchor="middle">M</text>
    </g>
    <line class="fold" x1="198" y1="590" x2="240" y2="840"/>
    <line class="fold" x1="203" y1="590" x2="245" y2="840"/>
  </g>

  <!-- right side wall: stacked box ends -->
  <g class="side-right">
    <g class="row-lines" stroke="var(--ink)" stroke-width="1.5">
      <line x1="790" y1="610" x2="930" y2="610"/><line x1="790" y1="633" x2="930" y2="633"/>
      <line x1="790" y1="656" x2="930" y2="656"/><line x1="790" y1="679" x2="930" y2="679"/>
      <line x1="790" y1="702" x2="930" y2="702"/><line x1="790" y1="725" x2="930" y2="725"/>
      <line x1="790" y1="748" x2="930" y2="748"/><line x1="790" y1="771" x2="930" y2="771"/>
      <line x1="790" y1="794" x2="930" y2="794"/><line x1="790" y1="817" x2="930" y2="817"/>
      <line x1="790" y1="840" x2="930" y2="840"/>
    </g>
    <g class="spine-rows">
      <g transform="rotate(180 860 599)"><text class="spine-dark" x="800" y="603">THC DRUG TESTING KIT</text><text class="brand" x="922" y="603" text-anchor="end">QTK</text></g>
      <g transform="rotate(180 860 622)"><text class="spine-dark" x="800" y="626">THC DRUG TESTING KIT</text><text class="brand" x="922" y="626" text-anchor="end">QTK</text></g>
      <g transform="rotate(180 860 645)"><text class="spine-dark" x="800" y="649">THC DRUG TESTING KIT</text><text class="brand" x="922" y="649" text-anchor="end">QTK</text></g>
      <g transform="rotate(180 860 668)"><text class="spine-dark" x="800" y="672">THC DRUG TESTING KIT</text><text class="brand" x="922" y="672" text-anchor="end">QTK</text></g>
      <g transform="rotate(180 860 691)"><text class="spine-dark" x="800" y="695">THC DRUG TESTING KIT</text><text class="brand" x="922" y="695" text-anchor="end">QTK</text></g>
      <g transform="rotate(180 860 714)"><text class="spine-dark" x="800" y="718">THC DRUG TESTING KIT</text><text class="brand" x="922" y="718" text-anchor="end">QTK</text></g>
      <g transform="rotate(180 860 737)"><text class="spine-dark" x="800" y="741">THC DRUG TESTING KIT</text><text class="brand" x="922" y="741" text-anchor="end">QTK</text></g>
      <g transform="rotate(180 860 760)"><text class="spine-dark" x="800" y="764">THC DRUG TESTING KIT</text><text class="brand" x="922" y="764" text-anchor="end">QTK</text></g>
      <g transform="rotate(180 860 783)"><text class="spine-dark" x="800" y="787">THC DRUG TESTING KIT</text><text class="brand" x="922" y="787" text-anchor="end">QTK</text></g>
      <g transform="rotate(180 860 806)"><text class="spine-dark" x="800" y="810">THC DRUG TESTING KIT</text><text class="brand" x="922" y="810" text-anchor="end">QTK</text></g>
      <g transform="rotate(180 860 829)"><text class="spine-dark" x="800" y="833">THC DRUG TESTING KIT</text><text class="brand" x="922" y="833" text-anchor="end">QTK</text></g>
    </g>
    <line class="fold" x1="930" y1="590" x2="888" y2="840"/>
    <line class="fold" x1="925" y1="590" x2="883" y2="840"/>
  </g>

  <!-- bottom lip: printed box fronts -->
  <g class="box-front box-three-in-one">
    <path class="cut" d="M415 845 V840 Q415 836 419 836 H481 Q485 836 485 840 V845"/>
    <rect x="343" y="845" width="12" height="60" fill="var(--board)"/>
    <g clip-path="url(#clipThreeInOne)">
      <rect x="355" y="845" width="60" height="50" fill="var(--red)"/>
      <rect x="355" y="895" width="60" height="35" fill="var(--green)"/>
      <rect x="355" y="930" width="60" height="30" fill="var(--navy)"/>
      <text class="box-word" transform="rotate(180 385 870)" x="385" y="880" text-anchor="middle" textLength="54" lengthAdjust="spacingAndGlyphs">MDMA</text>
      <text class="box-word" transform="rotate(180 385 912)" x="385" y="922" text-anchor="middle" textLength="48" lengthAdjust="spacingAndGlyphs">MET</text>
      <text class="box-word" transform="rotate(180 385 945)" x="385" y="955" text-anchor="middle" textLength="48" lengthAdjust="spacingAndGlyphs">THC</text>
    </g>
    <g transform="rotate(180 482 902)">
      <text class="box-name" x="423" y="857" textLength="118" lengthAdjust="spacingAndGlyphs">3 IN 1 DRUG TESTING KIT</text>
      <text class="box-small" x="423" y="872">THC 50ng/ml, METHAMPHETAMINE 300ng/ml</text>
      <text class="box-small" x="423" y="880">MDMA 500ng/ml (ecstasy)</text>
      <line x1="423" y1="883" x2="536" y2="883" stroke="var(--ink)" stroke-width="0.6"/>
      <text class="box-small" x="423" y="890">REF QT-301 · LOT 0724</text>
      <text class="brand" x="423" y="950">QTK</text>
      <text class="box-small" x="423" y="957">QUICK TEST KITS</text>
    </g>
    <path class="cut" d="M350 845 V955 Q350 960 355 960 H560 V845"/>
  </g>

  <g class="box-front box-thc">
    <path class="cut" d="M630 845 V840 Q630 836 634 836 H712 Q716 836 716 840 V845"/>
    <rect x="775" y="845" width="13" height="60" fill="var(--board)"/>
    <rect x="552" y="845" width="15" height="115" fill="var(--board)"/>
    <rect x="580" y="845" width="57" height="115" fill="var(--green)"/>
    <g stroke="#fff" stroke-width="2"><line x1="580" y1="890" x2="637" y2="890"/><line x1="580" y1="928" x2="637" y2="928"/></g>
    <text class="box-word" transform="rotate(180 608 868)" x="608" y="878" text-anchor="middle" textLength="46" lengthAdjust="spacingAndGlyphs">THC</text>
    <text class="box-word" transform="rotate(180 608 909)" x="608" y="919" text-anchor="middle" textLength="46" lengthAdjust="spacingAndGlyphs">THC</text>
    <text class="box-word" transform="rotate(180 608 944)" x="608" y="954" text-anchor="middle" textLength="46" lengthAdjust="spacingAndGlyphs">THC</text>
    <g transform="rotate(180 705 902)">
      <text class="box-name" x="646" y="857" textLength="116" lengthAdjust="spacingAndGlyphs">THC DRUG TESTING KIT</text>
      <text class="box-small" x="646" y="872">THC 50ng/ml · MARIJUANA · CANNABIS</text>
      <line x1="646" y1="883" x2="762" y2="883" stroke="var(--ink)" stroke-width="0.6"/>
      <text class="box-small" x="646" y="890">REF QT-101 · LOT 0724</text>
      <text class="brand" x="646" y="950">QTK</text>
      <text class="box-small" x="646" y="957">QUICK TEST KITS</text>
    </g>
    <path class="cut" d="M565 845 V960 H775 Q780 960 780 955 V845"/>
  </g>

  <!-- divider insert -->
  <g class="divider-insert">
    <path d="M812 78 L922 68 L968 108 L1030 96 L1120 160 L928 446 L908 436 L900 382 L862 425 L843 425 Z" fill="var(--board)"/>
    <path class="cut" d="M818 84 L920 74 L968 115 L1028 103 L1110 162 L926 438 L913 430 L903 376 L863 419 L848 419 Z"/>
    <g class="fold">
      <line x1="820" y1="126" x2="966" y2="112"/>
      <line x1="966" y1="112" x2="898" y2="376"/>
      <line x1="970" y1="112" x2="902" y2="376"/>
      <line x1="970" y1="112" x2="1090" y2="193"/>
      <line x1="845" y1="382" x2="898" y2="376"/>
      <line x1="902" y1="376" x2="946" y2="405"/>
    </g>
  </g>
</svg>
</main>
</body>
</html>
```